Business Card and Letterhead for Juniper Anvil - (Have Logo)

Update 4: Removed company reg no from business card details as it looked a bit out of place. Updated services list.
UPDATE 3
Sorry, I got the address a little bit wrong, have updated it below. Sorry for any inconvenience caused.
UPDATE 2
Finally I have the details for the business cards and letterhead. Submissions already made do not have to be updated unless shortlisted, if all new submissions could include the details for me, Marcus, that would be very much appreciated and help with the final shortlist selection. I intend to share a shortlist of the three best entries with past and existing customers for their feedback and opinions. Thank you all again for your time.
Here are the details.
Marcus Telby
Web Developer
T: 01632 960 418
E: marcus@juniperanvil.example
www.juniperanvil.example
Professional Photography
Web Solutions & E-Commerce
Audio & HD Video Production
Marketing & Promotions
Identity and Branding
Juniper Anvil Ltd
Suite 20938, 3rd Floor
212-224 Orchard Lane
London, N7 9QX
Company Reg. No: 05829147
The order and the layout of the information are of course down to the design, but the company registration number should be smaller and less prominent. The formatting of the telephone and email address using a T: and an E: I am not sure about and again if it is Tel: or Email: or Icons is up to the design.
The Company No. on the letterhead should read (somewhere in small text along the bottom):
Juniper Anvil is a Ltd Company registered in England & Wales, Registration No. 05829147.
The second business card details are
Oliver Brackley
Photographer
T: 01632 960 418
E: oliver@juniperanvil.example
Everything else the same of course.
Thank you again for all the submissions so far.
END OF UPDATE 2
-
UPDATE 1: Please do not alter the logo nor the logo colours. (This was a previous pixel forum project and I am extremely happy with it. The icon can stand alone of course, but I have had to eliminate all entries that have made it black and white, or reversed the icon.) I would like to thank everyone that has participated so far and am very grateful for all your thought and time.
End of Update 1
-
Original Brief:
I have attached the logo vector file.
Following a superb logo from a previous Pixel Forum project I am now looking for a business card design and (although less important) a letterhead as well.
I must admit I tried to do it myself but could only come up with the usual amateur stuff that in comparison to the quality of the logo looked awful.
About Us
Juniper Anvil Ltd will be a new company due to start in January. It is really just me (a web developer) and my friend (a photographer). We will be aiming at the usual small to medium sized businesses in the local area, selling various digital services including photographic services to the public, web hosting and development, commercial photography, modelling services (not us!), full video and film production and possibly a bit of marketing as well. (Really it is anything we can do professionally all lumped together! We met running seperate businesses which have both since closed)
We will not be competing on price. We plan to be expensive but fair. Certainly not the cheapest.
What we are looking for
Business Card
I imagine a double sided business card, which will be used for more than one person. I imagine the front to be the same for everyone and the persons details to be on the back, although this is of course only my thoughts and I am of course completely open to any ideas.
The card could also have a services list or a bit about what we do on it. It might feature the website address, our business address (mail forwarding address) or our registered company number.
Or it might have none of that, we are completely open to any ideas and have no real fixed opinions. I just want it to be really nice :-)
Letterhead (secondary importance)
We will make our decision primarily on the business card, although a mathcing letterhead would be fantastic. Something standardish in format and simple, although again, all ideas are welcomed.
I hope that is enough information but if you have any questions I will answer them as fully and as quickly as possible.
Thank you once again and I really look forward to seeing your ideas and picking a winner.
Marcus T.
Small businesses AND the general public
Film Production

```html
<!DOCTYPE html>
<html lang="en">
<head>
<meta charset="utf-8">
<title>Juniper Anvil — Business Card</title>
<link rel="stylesheet" href="https://fonts.googleapis.com/css2?family=Archivo:wght@500;700;800&display=swap">
<style>
  :root {
    --brand-red: #b5121b;
    --brand-grey: #4a4a4c;
    --card-white: #ffffff;
    --card-black: #000000;
    --page-bg: #ffffff;
  }
  * { margin: 0; padding: 0; box-sizing: border-box; }
  html, body {
    width: 1200px; height: 900px; overflow: hidden;
    background: var(--page-bg);
    font-family: "Archivo", Arial, sans-serif;
  }
  .stage { position: relative; width: 1200px; height: 900px; }

  .card {
    position: absolute;
    width: 400px; height: 570px;
    box-shadow: 2px 3px 6px rgba(0,0,0,0.35);
  }

  /* Front: personal details */
  .card-front {
    left: 200px; top: 170px;
    background: var(--card-white);
    text-align: right;
    padding: 40px 34px 0 30px;
    text-transform: uppercase;
    letter-spacing: 0.12em;
    font-weight: 700;
  }
  .person-name { color: var(--brand-red); font-size: 22px; font-weight: 800; line-height: 1.1; }
  .person-role { color: var(--brand-grey); font-size: 15px; margin-top: 2px; }
  .phone-list { color: var(--brand-grey); font-size: 16px; line-height: 1.25; margin-top: 36px; }
  .phone-list span { margin-left: 10px; }
  .email { color: var(--brand-red); font-size: 12px; margin-top: 78px; }
  .address { color: var(--brand-grey); font-size: 11px; line-height: 1.45; margin-top: 4px; }
  .website { color: var(--brand-red); font-size: 12px; margin-top: 58px; }

  .front-mark {
    position: absolute; left: 30px; top: 400px;
    display: flex; align-items: center; gap: 8px;
    color: var(--brand-red); font-size: 13px; font-weight: 800;
  }
  .front-mark .square { width: 22px; height: 22px; background: var(--brand-grey); }

  .services {
    position: absolute; right: 34px; bottom: 40px;
    color: var(--brand-grey); font-size: 10.5px; line-height: 1.35;
    list-style: none;
  }

  /* Back: brand side */
  .card-back {
    left: 640px; top: 170px;
    background: var(--card-black);
    text-align: center;
    text-transform: uppercase;
    letter-spacing: 0.12em;
    font-weight: 700;
  }
  .back-mark {
    position: absolute; left: 0; right: 0; top: 130px;
    display: flex; flex-direction: column; align-items: center; gap: 18px;
  }
  .back-mark .square { width: 120px; height: 48px; background: var(--brand-grey); }
  .back-mark .brand-name { color: var(--brand-red); font-size: 34px; font-weight: 800; letter-spacing: 0.08em; }
  .tagline {
    position: absolute; left: 0; right: 0; top: 318px;
    color: var(--brand-red); font-size: 14px; line-height: 1.3;
  }
  .tagline em { font-style: italic; }
  .back-signature {
    position: absolute; left: 0; right: 0; bottom: 24px;
    color: var(--brand-red); font-size: 15px; font-weight: 800;
  }
</style>
</head>
<body>
<main class="stage">

  <section class="card card-front">
    <h1 class="person-name">Theo Marlow</h1>
    <p class="person-role">Photography</p>
    <p class="phone-list">Office<span>07700-900123</span><br>Mobile<span>07700-900456</span></p>
    <p class="email">theo@juniperanvil.example</p>
    <p class="address">18 Willowmere Road<br>London<br>N7 4RT<br>United Kingdom</p>
    <p class="website">www.juniperanvil.example</p>
    <div class="front-mark"><span class="square"></span>Juniper Anvil</div>
    <ul class="services">
      <li>Marketing</li>
      <li>Web Hosting</li>
      <li>Photography</li>
      <li>Modeling Services</li>
      <li>Website Development</li>
      <li>Commericial Photography</li>
      <li>Full Video &amp; Film Production</li>
    </ul>
  </section>

  <section class="card card-back">
    <div class="back-mark">
      <span class="brand-name">Juniper Anvil</span>
      <span class="square"></span>
    </div>
    <p class="tagline">It’s still your business -<br>just more <em>delicious.</em></p>
    <p class="back-signature">Juniper Anvil</p>
  </section>

</main>
</body>
</html>
```